Young Accounting firm needing a captivating business card

We need a business card design that forces the person to look at the card because its either gold foil, plastic, or lettering pop up etc. We already have a logo with a specific gold color and we need to make it pop. We are an accounting firm. I need the words" accounting, payroll, licenses, audits, taxes" somewhere on the business card so as to describe what we do- preferably on the side where the logo is at.

Industry/Entity Type

Accounting

Contact Information for Business Card

Address 48207 9th Ave N Ste 305, Cedar Hollow, WA 98512
Business Phone (360)418-2967
Fax (360)418-2051
Office Cell Phone (360)506-7139

Font styles to use
Serif

Colors
85abd2

Requirements
Must have
• It should state
• "Accounting" "Taxes" "Audits" "Licenses" "Payroll"
Nice to have
• Matte with gold foil, different textures, With Either a textured ivory background or gray blue slate background
Should not have
• colorful colors

```html
<!DOCTYPE html>
<html lang="en">
<head>
<meta charset="utf-8">
<title>Northvale Tax – Business Card</title>
<link href="https://fonts.googleapis.com/css2?family=Heebo:wght@400;500&display=swap" rel="stylesheet">
<style>
  :root {
    --backdrop: #1d1d1d;
    --card-black: #151515;
    --gold: #c9a04c;
    --gold-light: #e9cf7e;
    --gold-dark: #8a6a2a;
  }
  * { margin: 0; padding: 0; box-sizing: border-box; }
  html, body {
    width: 1200px; height: 900px; overflow: hidden;
    background: var(--backdrop);
    font-family: "Heebo", Arial, sans-serif;
  }
  .canvas {
    position: relative; width: 1200px; height: 900px;
    background: radial-gradient(ellipse at 50% 40%, #2e2e2e 0%, var(--backdrop) 70%);
  }
  .card {
    position: absolute; left: 250px; width: 700px; height: 400px;
    border-radius: 4px; overflow: hidden;
    box-shadow: 0 18px 40px rgba(0,0,0,.55);
  }
  .card-back { top: 40px; background: var(--card-black); }
  .card-front { top: 470px; background: var(--card-black); padding: 38px 44px; }

  .back-pattern {
    position: absolute; inset: 0;
    background: linear-gradient(120deg, var(--gold-dark) 0%, #b39a5a 45%, #d3c088 60%, var(--gold-dark) 100%);
  }
  .back-name {
    position: absolute; left: 50%; top: 50%;
    transform: translate(-50%, -50%);
    background: var(--card-black);
    color: var(--gold-light);
    font-size: 40px; font-weight: 500; letter-spacing: -0.5px;
    padding: 6px 26px; border-radius: 40px;
    white-space: nowrap;
  }

  .brand { display: flex; align-items: center; gap: 16px; }
  .brand-mark { width: 46px; height: 46px; background: var(--gold-light); }
  .brand-name { color: var(--gold); font-size: 44px; font-weight: 400; letter-spacing: -1px; line-height: 1; }

  .person { margin-top: 26px; }
  .person-name { color: var(--gold); font-size: 30px; font-weight: 500; line-height: 1.05; }
  .person-role { color: var(--gold-dark); font-size: 15px; }

  .details { display: flex; gap: 60px; margin-top: 18px; color: var(--gold); font-size: 16px; line-height: 1.45; }
  .address { font-style: normal; }
  .contact-list { list-style: none; }
  .contact-list li { display: flex; align-items: center; gap: 8px; }
  .contact-list svg { width: 11px; height: 11px; fill: var(--gold); flex: none; }

  .services {
    position: absolute; left: 44px; bottom: 28px;
    color: var(--gold); font-size: 16px;
  }
  .services strong { font-weight: 500; }
</style>
</head>
<body>
<div class="canvas">

  <section class="card card-back">
    <div class="back-pattern" role="img" aria-label="Repeating gold geometric brand pattern"></div>
    <div class="back-name">Northvale Tax</div>
  </section>

  <section class="card card-front">
    <div class="brand">
      <span class="brand-mark"></span>
      <span class="brand-name">Northvale Tax</span>
    </div>

    <div class="person">
      <div class="person-name">Daniel Reyes</div>
      <div class="person-role">Director</div>
    </div>

    <div class="details">
      <address class="address">
        48207 9th Ave N Ste 305,<br>Cedar Hollow, WA 98512
      </address>
      <ul class="contact-list">
        <li><svg viewBox="0 0 12 12"><path d="M2 1h3l1 3-2 1a7 7 0 0 0 3 3l1-2 3 1v3c-6 0-9-3-9-9z"/></svg>(360)418-2967</li>
        <li><svg viewBox="0 0 12 12"><path d="M3 1h5v3H3zM1 5h10v6H1zM3 7h6v2H3z"/></svg>(360)418-2051</li>
        <li><svg viewBox="0 0 12 12"><path d="M3 0h6v12H3zM4 1v9h4V1z"/></svg>(360)506-7139</li>
        <li><svg viewBox="0 0 12 12"><path d="M0 2h12v8H0zM1 3v.5l5 3.5 5-3.5V3z"/></svg>info@northvaletax.com</li>
        <li><svg viewBox="0 0 12 12"><circle cx="6" cy="6" r="6"/></svg>www.northvaletax.com</li>
      </ul>
    </div>

    <p class="services">Accounting | <strong>Payroll</strong> | Licenses | Audits | Taxes</p>
  </section>

</div>
</body>
</html>
```